AUTOMOTIVE/ CAR REPAIRS / CRASH REPAIRS / PAINT SPRAYING AND PANEL BEATING

AUTOMOTIVE REPAIR. CAR / MOTORCYCLES GOT LOGO DESIGN / DID THINK ABOUT SOCIA DONT NOALREADY HAVE WEB ADRESS www.brentavel.co.uk and mail sales@brentavel,co.uk NEED SOMETHINK I CAN MANAGE TO UPLOAD PICTURES IN TO A GALLERY OR SOMETHINGLIKE THAT I ALSO SELL CAR AND MOTORCYCLES MAYBE A SELLS PAGE WITH A QUIDLOOP LINK

Target Market(s)

TRADE / GENERAL PUBLIC

Industry/Entity Type

Automotive

Coding

Coded - Design and coding required

Number of Pages Required

4 page

Font styles to use
Serif
Sans Serif

Colors

Designer to choose colors to be used in the design.

Requirements
Must have
• GALLERY/ SHOP TO SALE CARS AND MOTORCYCLE / LOGOS OF MATERIALS I USE TORVENDE / KELP / SANVITE / Q BAND / GLIDECARE
• CONTACT US
Nice to have
• QUIDLOOP / EASY TO MANAGE / VIDEO CLIP OF TORVENDE TINT PLANNER Q7
• SWIFT BLEND PAINT LUMINEL HYDROLUX AND PELOVAN

```html
<!DOCTYPE html>
<html lang="en">
<head>
<meta charset="utf-8">
<title>Brentavel Bodyshop</title>
<link href="https://fonts.googleapis.com/css2?family=Audiowide&family=Montserrat:wght@400;500;600;700&display=swap" rel="stylesheet">
<style>
:root{
  --ink:#1b1c22;
  --ink-2:#24252c;
  --red:#e3141f;
  --red-deep:#7e111a;
  --grey:#3a3b40;
  --white:#ffffff;
  --muted:#cfd0d4;
  --display:'Audiowide', sans-serif;
  --body:'Montserrat', sans-serif;
}
*{box-sizing:border-box;margin:0;padding:0}
html,body{width:1200px;height:3651px;overflow:hidden;background:var(--ink)}
body{font-family:var(--body);color:var(--white)}
.page{position:relative;width:1200px;height:3651px;overflow:hidden;background:var(--ink)}
.abs{position:absolute}
.btn-skew{position:absolute;display:flex;align-items:center;justify-content:center;gap:8px;font:700 16px var(--body);color:var(--white);background:var(--red);transform:skewX(-20deg)}
.btn-skew span{transform:skewX(20deg);display:flex;align-items:center;gap:8px}
.btn-skew::before,.btn-skew::after{content:"";position:absolute;top:0;bottom:0;width:4px;background:var(--red)}
.btn-skew::before{left:-10px}.btn-skew::after{right:-10px}
.arrow-dot{width:15px;height:15px;border-radius:50%;background:currentColor;position:relative;display:inline-block}
.arrow-dot::after{content:"";position:absolute;left:4px;top:4px;border-left:7px solid var(--red);border-top:3.5px solid transparent;border-bottom:3.5px solid transparent}
/* header */
.site-header{top:0;left:0;width:1200px;height:80px;background:var(--ink)}
.brand{left:145px;top:14px;text-align:center}
.brand-name{font:400 29px var(--display);letter-spacing:2px}
.brand-sub{font:500 11px var(--body);letter-spacing:9px;margin-top:2px}
.main-nav{left:463px;top:31px;display:flex;gap:30px;font:500 13.5px var(--body)}
.main-nav .active{color:var(--red)}
.cart{left:1023px;top:25px;width:30px;height:30px;border-radius:50%;background:var(--red)}
/* hero */
.hero-photo{top:80px;left:0;width:1200px;height:520px;background:linear-gradient(100deg,#b0101e 0%,#3a0d1a 22%,#0f6c73 34%,#1a1d2a 48%,#1a1b24 70%,#23121c 100%)}
.hero-title{left:606px;top:235px;font:400 62px/66px var(--display)}
.hero-sub{left:606px;top:380px;font:700 19.5px/30px var(--body);width:470px}
.dots{left:1133px;top:330px;display:flex;flex-direction:column;gap:17px}
.dots i{width:10px;height:10px;border-radius:50%;background:var(--white);display:block}
.dots i.on{background:none;border:2px solid var(--white)}
/* headings */
.mark{width:50px;height:50px;border-radius:50%;background:radial-gradient(circle at 35% 35%,#f3f3f3,#9a9ba0 60%,var(--red) 61%)}
.h-sec{font:400 40px var(--display);white-space:nowrap}
.h-sec em{font-style:normal;color:var(--red)}
.about-text{left:146px;top:815px;width:460px;font:400 14px/29.6px var(--body)}
.about-art{left:655px;top:720px;width:400px;height:400px;border-radius:50%;background:radial-gradient(circle at 40% 60%,#e9e9eb 0%,#8d8e93 35%,#c3101c 36%,#6b0b13 75%,#1b1c22 76%)}
/* services */
.svc{position:absolute;width:270px}
.svc h3{font:700 16px var(--body);margin-bottom:10px}
.svc p{font:400 12.5px/19px var(--body)}
.svc-icon{position:absolute;width:48px;height:48px}
.svc-hub{left:510px;top:1375px;width:180px;height:180px;border-radius:50%;background:radial-gradient(circle at 40% 60%,#ececec,#8e8f95 45%,var(--red) 46%,#5c0a12 80%)}
.view-more{left:512px;top:1625px;width:176px;height:37px;background:var(--white);color:var(--red);font-size:15px}
.view-more::before,.view-more::after{background:var(--white)}
.view-more .arrow-dot{color:var(--red)}
.view-more .arrow-dot::after{border-left-color:var(--white)}
.cars{left:185px;top:1705px;width:840px;height:255px;border-radius:120px 120px 60px 60px;background:linear-gradient(90deg,#e8901c 0%,#3b3c41 22%,#c82625 50%,#7fd23a 75%,#2b2c30 100%)}
/* gallery */
.gallery{left:145px;top:2145px;display:grid;grid-template-columns:repeat(3,296px);grid-auto-rows:227px;gap:11px}
.gallery div{width:296px;height:227px}
.brands{left:144px;top:2652px;display:flex;gap:23px}
.brands div{width:160px;height:62px;background:var(--white);display:flex;align-items:center;justify-content:center;font:700 19px var(--body);color:var(--red)}
.brands div.blue{background:#1f4e9c;color:var(--white)}
/* booking */
.addr{left:0;width:1200px;top:3010px;text-align:center;font:500 16.5px var(--body)}
.field{position:absolute;top:3068px;width:263px;height:49px;border:1px solid #8c8d92;font:500 12px var(--body);display:flex;align-items:center;justify-content:space-between;padding:0 20px;color:var(--muted)}
.note{left:0;width:1200px;top:3150px;text-align:center;font:400 19.5px/30px var(--body)}
.btn-pill{left:455px;top:3238px;width:286px;height:57px;border-radius:29px;background:var(--red);display:flex;align-items:center;justify-content:center;gap:10px;font:700 18px var(--body)}
/* footer */
.social{left:502px;top:3413px;display:flex;gap:12px}
.social span{width:40px;height:40px;border-radius:50%;border:1.5px solid var(--white);display:flex;align-items:center;justify-content:center;font:600 8.5px var(--body)}
.contact-line{left:0;width:1200px;top:3476px;text-align:center;font:400 13px var(--body)}
.contact-line b{color:var(--red);font-weight:700;margin:0 4px}
.foot-nav{left:0;width:1200px;top:3513px;text-align:center;font:700 16px var(--body);word-spacing:3px}
.copy{left:0;width:1200px;top:3550px;text-align:center;font:400 12px var(--body)}
.cards{left:503px;top:3585px;display:flex;gap:6px}
.cards span{width:34px;height:21px;background:var(--white);color:var(--ink);border-radius:2px;font:700 5px var(--body);display:flex;align-items:center;justify-content:center}
</style>
</head>
<body>
<div class="page">

  <!-- hero -->
  <div class="abs hero-photo" role="img" aria-label="Red and teal lit sports car front corner in a dark studio"></div>
  <svg class="abs" style="top:540px;left:0" width="1200" height="180" viewBox="0 0 1200 180">
    <path d="M0 40 L600 160 L1200 40 L1200 0 L0 0 Z" fill="none"/>
    <path d="M0 20 L0 60 L600 170 L1200 60 L1200 20 L600 140 Z" fill="var(--ink)"/>
    <path d="M190 52 L600 165 L1010 52 L990 52 L600 135 L210 52 Z" fill="var(--red)"/>
    <path d="M420 110 L600 168 L780 110 L600 150 Z" fill="#a30d17"/>
  </svg>
  <div class="abs hero-title">BRENTAVEL<br>BODYSHOP</div>
  <div class="abs hero-sub">Fully qualified trained technicians family run business established over 30 years</div>
  <div class="btn-skew" style="left:620px;top:478px;width:230px;height:46px">
    <span>APPOINTMENT <i class="arrow-dot"></i></span>
  </div>
  <div class="abs dots"><i></i><i></i><i class="on"></i><i></i><i></i></div>

  <!-- header -->
  <header class="abs site-header">
    <div class="abs brand">
      <div class="brand-name">BRENTAVEL</div>
      <div class="brand-sub">BODYSHOP</div>
    </div>
    <nav class="abs main-nav">
      <span class="active">HOME</span><span>ABOUT US</span><span>SERVICES</span><span>CUSTOM</span><span>GALLERY</span><span>CONTACT</span>
    </nav>
    <div class="abs cart"></div>
  </header>

  <!-- about -->
  <div class="abs mark" style="left:146px;top:688px"></div>
  <h2 class="abs h-sec" style="left:146px;top:752px">ABOUT <em>US</em></h2>
  <p class="abs about-text">Brentavel, based in Oakridge, Derbyshire established in August, 1985 has grown to become Derbyshire's premiere manufacturer approved accident repair centre.<br>&nbsp;Equipped with the latest technology and factory trained technicians, we process accident repairs for all leading insurance and vehicle management companies, specialising in accident repairs for most prestige vehicles manufacturers.</p>
  <div class="btn-skew" style="left:153px;top:1048px;width:174px;height:37px;font-size:15px">
    <span>READ MORE <i class="arrow-dot"></i></span>
  </div>
  <div class="abs about-art"></div>

  <!-- services -->
  <svg class="abs" style="top:1160px;left:0" width="1200" height="620" viewBox="0 0 1200 620">
    <defs>
      <linearGradient id="svcFill" x1="0" y1="0" x2="0" y2="1">
        <stop offset="0" stop-color="#b51822"/><stop offset="1" stop-color="#7a0f18"/>
      </linearGradient>
    </defs>
    <ellipse cx="610" cy="310" rx="860" ry="305" fill="var(--red)"/>
    <ellipse cx="600" cy="320" rx="850" ry="300" fill="url(#svcFill)"/>
  </svg>
  <h2 class="abs h-sec" style="left:0;width:1200px;text-align:center;top:1248px">OUR SERVICES</h2>

  <svg class="svc-icon" style="left:148px;top:1360px" viewBox="0 0 48 48" fill="none" stroke="#fff" stroke-width="2"><rect x="10" y="14" width="22" height="8"/><path d="M32 18h10M20 22v14M14 36h12M18 6h6v8"/></svg>
  <div class="svc" style="left:226px;top:1360px"><h3>FULL OR PART RESPRAYS</h3><p>Single panel resprays to full<br>car resprays</p></div>

  <svg class="svc-icon" style="left:722px;top:1360px" viewBox="0 0 48 48" fill="none" stroke="#fff" stroke-width="2"><path d="M8 40L30 18M18 8l22 22M34 8a6 6 0 0 0 6 6"/></svg>
  <div class="svc" style="left:800px;top:1355px"><h3>BUMPER REPAIR</h3><p>Bumper scuffs, plastic bumper repairs and full bumper replacements.Full factory matched colours.</p></div>

  <svg class="svc-icon" style="left:155px;top:1497px" viewBox="0 0 48 48" fill="none" stroke="#fff" stroke-width="2"><path d="M10 30L28 12l10 10-18 18H10z M6 44h36"/></svg>
  <div class="svc" style="left:226px;top:1497px"><h3>DENT &amp; SCRATCH REMOVAL</h3><p>From small paintless dent repairs to full panel replacements. Scratches, chips &amp; paint repairs undertaken</p></div>

  <svg class="svc-icon" style="left:705px;top:1497px;width:64px" viewBox="0 0 64 48" fill="none" stroke="#fff" stroke-width="2"><path d="M4 32h56v-8l-8-4-6-10H18l-6 10-8 4z"/><circle cx="16" cy="36" r="5"/><circle cx="48" cy="36" r="5"/></svg>
  <div class="svc" style="left:800px;top:1497px"><h3>ACCIDENT REPAIR</h3><p>All accident repair undertaken. Just one call to Brentavel and we'll help you take the first steps towards &gt;&gt;</p></div>

  <div class="abs svc-hub"></div>
  <div class="btn-skew view-more"><span>VIEW MORE <i class="arrow-dot"></i></span></div>
  <div class="abs cars" role="img" aria-label="Row of restored cars: orange hatchback, black muscle car, red classic roadster, green hatchback and an engine"></div>

  <!-- gallery -->
  <div class="abs mark" style="left:575px;top:2000px"></div>
  <h2 class="abs h-sec" style="left:0;width:1200px;text-align:center;top:2060px">OUR <em>GALLERY</em></h2>
  <div class="abs gallery">
    <div role="img" aria-label="Airbrushed custom paint artwork" style="background:linear-gradient(135deg,#d9dde3,#4b7cb8 50%,#c79a3b)"></div>
    <div role="img" aria-label="Red classic car shell being restored in workshop" style="background:linear-gradient(180deg,#8d9096,#c7191b 55%,#b9bec6)"></div>
    <div role="img" aria-label="Silver sports car in spray booth" style="background:linear-gradient(135deg,#3a3b33,#b7b8b4 50%,#d3cf8c)"></div>
    <div role="img" aria-label="Black saloon car in the workshop" style="background:linear-gradient(180deg,#5f6f86,#141519 50%,#9aa3b0)"></div>
    <div role="img" aria-label="Motorcycle handlebars against a sunset sky" style="background:linear-gradient(180deg,#8d8c88,#4a4a48 50%,#151515)"></div>
    <div role="img" aria-label="Motorcycle tank in pink primer" style="background:linear-gradient(135deg,#d8d3d6,#b27a96 50%,#8d5a74)"></div>
  </div>
  <div class="abs brands">
    <div>TORVENDE</div><div style="color:var(--ink)">KELP</div><div class="blue">SANVITE</div><div>Q BAND</div><div style="color:#1f4e9c">GLIDECARE</div>
  </div>

  <!-- booking -->
  <svg class="abs" style="top:2790px;left:0" width="1200" height="600" viewBox="0 0 1200 600">
    <ellipse cx="620" cy="295" rx="930" ry="295" fill="var(--red)"/>
    <ellipse cx="600" cy="300" rx="910" ry="282" fill="var(--grey)"/>
  </svg>
  <div class="abs mark" style="left:575px;top:2870px"></div>
  <h2 class="abs h-sec" style="left:0;width:1200px;text-align:center;top:2935px">BOOK AN <em>APPOINTMENT</em></h2>
  <p class="abs addr">Brentavel Bodyshop, Harrowgate Trade Park, Fen Lane, Oakridge, Derbyshire, DW55 9QX</p>
  <div class="field" style="left:187px">DATE <span>&#9633;</span></div>
  <div class="field" style="left:468px">TIME <span>&#9675;</span></div>
  <div class="field" style="left:749px">PRICE <span>$</span></div>
  <p class="abs note">If you are unable to keep your appointment,<br>Please contact us as soon as possible</p>
  <div class="abs btn-pill">APPOINTMENT NOW <i class="arrow-dot" style="color:#fff"></i></div>

  <!-- footer -->
  <div class="abs social"><span>Socia</span><span>Chirp</span><span>Plusly</span><span>Linkro</span></div>
  <p class="abs contact-line"><b>&#9679;</b> brentavel.co.uk &nbsp;| <b>&#9742;</b> 07700 900417 &nbsp;| <b>&#9993;</b> sales@brentavel.co.uk</p>
  <p class="abs foot-nav">HOME &nbsp;/ &nbsp;ABOUT US &nbsp;/ &nbsp;SERVICE &nbsp;/ &nbsp;CUSTOM &nbsp;/ &nbsp;GALLERY &nbsp;/ &nbsp;CONTACT</p>
  <p class="abs copy">Copyrights © 2019, Brentavel.All rights reserved &nbsp;| &nbsp;Privacy policy &nbsp;| &nbsp;Site Map</p>
  <div class="abs cards"><span>CARDWELL</span><span>DUOCARD</span><span>FARPAY</span><span>AMEREL</span><span>QUIDLOOP</span></div>
</div>
</body>
</html>
```